Need simple and modern looking business card with all my information on one side and logo on the other side
Info :
Company name - VELMAR CONSTRUCTION LLC
Company addres- 418 harbor 87th. Dunmoor park ny 10352
Email- velmarllc@tridomail.Com
Company phone number 555-318-6094
Cell number- 555-742-0583
Web site - velmarllc.Com
My name Gerald tomasino

Target Market(s)

Construction , home improvement, remodeling

Industry/Entity Type

Construction

Contact Information for Business Card

It has to be moder but at the same time simple

Font styles to use
Sans Serif

Colors
0255a3
ffffff
000000
f78f20
b1b1b1
9d9d9d
1b1b1b
33a6d7
ec1f27

Requirements
Must have
• My logo on one side maybe with a some kind of background on the other side all my information
Nice to have
• Some kind of background pictures provided by you .PLEASE HAVE ACCOUNT WITH PIXELVAULT WILL NOT PAY ANY EXTRA FEES .
Should not have
• Any kind of hamer, nails,screws, helmets itp. Please do not copy the other designs come up with something new.

```html
<!DOCTYPE html>
<html lang="en">
<head>
<meta charset="utf-8">
<title>Velmar Construction LLC – Business Card</title>
<link href="https://fonts.googleapis.com/css2?family=Open+Sans:wght@400;600&display=swap" rel="stylesheet">
<style>
  :root {
    --blue: #0255a3;
    --white: #ffffff;
    --black: #000000;
    --orange: #f78f20;
    --grey-light: #b1b1b1;
    --grey: #9d9d9d;
    --ink: #1b1b1b;
    --sky: #33a6d7;
    --red: #ec1f27;
    --stage: #e4e4e4;
    --text-muted: #8a8a8a;
  }
  * { margin: 0; padding: 0; box-sizing: border-box; }
  html, body {
    width: 1200px; height: 900px; overflow: hidden;
    background: var(--stage);
    font-family: "Open Sans", sans-serif;
  }
  .canvas {
    position: relative; width: 1200px; height: 900px;
    display: flex; flex-direction: column; align-items: center;
    justify-content: center; gap: 30px;
  }
  .card {
    position: relative; width: 700px; height: 400px;
    background: var(--white); border-radius: 22px; overflow: hidden;
    box-shadow: 0 6px 18px rgba(0,0,0,0.12);
  }
  .brand {
    display: flex; align-items: center; gap: 12px;
    color: var(--ink); font-weight: 600; letter-spacing: 1px;
  }
  .brand-square { width: 18px; height: 18px; background: var(--orange); flex: none; }

  /* front */
  .site-backdrop {
    position: absolute; inset: 0;
    background: linear-gradient(180deg, rgba(255,255,255,0) 0%, rgba(214,212,206,0.55) 55%, rgba(200,194,182,0.6) 100%);
  }
  .card-front .brand {
    position: absolute; left: 50%; top: 50%;
    transform: translate(-50%, -50%); font-size: 30px;
  }

  /* back */
  .swoosh { position: absolute; inset: 0; }
  .card-back .brand {
    position: absolute; left: 70px; top: 120px; font-size: 22px;
  }
  .holder {
    position: absolute; right: 70px; top: 52px;
    font-size: 24px; letter-spacing: 0.5px; color: var(--ink);
  }
  .holder .first { color: var(--orange); }
  .address {
    position: absolute; left: 70px; top: 200px;
    font-size: 14px; line-height: 22px; color: var(--grey);
  }
  .contact-strip {
    position: absolute; left: 0; top: 262px; width: 34px; height: 112px;
    background: var(--orange); border-radius: 0 8px 8px 0;
    display: flex; flex-direction: column; justify-content: space-around; align-items: center;
    padding: 4px 0;
  }
  .contact-strip svg { width: 16px; height: 16px; }
  .contacts {
    position: absolute; left: 70px; top: 264px;
    list-style: none; font-size: 15px; line-height: 27px; color: #6f6f6f;
  }
</style>
</head>
<body>
<main class="canvas">

  <section class="card card-front" aria-label="Business card front">
    <div class="site-backdrop" role="img" aria-label="Faint photo of a construction site with cranes and rising buildings"></div>
    <div class="brand"><span class="brand-square"></span>VELMAR CONSTRUCTION LLC</div>
  </section>

  <section class="card card-back" aria-label="Business card back">
    <svg class="swoosh" viewBox="0 0 700 400" width="700" height="400" aria-hidden="true">
      <rect x="0" y="390" width="700" height="10" fill="var(--blue)"/>
      <path d="M700,140 C650,270 520,360 300,392 L300,400 L700,400 Z" fill="var(--blue)"/>
      <path d="M700,132 C652,262 525,352 320,392 L700,400 Z" fill="var(--white)"/>
      <path d="M700,108 C660,240 540,345 360,400 L700,400 Z" fill="var(--ink)"/>
    </svg>

    <div class="brand"><span class="brand-square"></span>VELMAR CONSTRUCTION LLC</div>

    <h1 class="holder"><span class="first">GERALD</span> TOMASINO</h1>

    <p class="address">418 Harbor 87th.<br>Dunmoor Park NY 10352</p>

    <div class="contact-strip" aria-hidden="true">
      <svg viewBox="0 0 16 16"><path d="M4 2 L6 5 L5 6.5 C6 8.5 7.5 10 9.5 11 L11 10 L14 12 L12.5 14 C7 13.5 2.5 9 2 3.5 Z" fill="var(--white)"/></svg>
      <svg viewBox="0 0 16 16"><rect x="4.5" y="1.5" width="7" height="13" rx="1.5" fill="none" stroke="var(--white)" stroke-width="1.4"/><circle cx="8" cy="12" r="0.9" fill="var(--white)"/></svg>
      <svg viewBox="0 0 16 16"><rect x="1.5" y="3.5" width="13" height="9" fill="none" stroke="var(--white)" stroke-width="1.4"/><path d="M1.5 3.5 L8 9 L14.5 3.5" fill="none" stroke="var(--white)" stroke-width="1.4"/></svg>
      <svg viewBox="0 0 16 16"><circle cx="8" cy="8" r="6.3" fill="none" stroke="var(--white)" stroke-width="1.3"/><ellipse cx="8" cy="8" rx="2.7" ry="6.3" fill="none" stroke="var(--white)" stroke-width="1.1"/><path d="M1.7 8 H14.3" stroke="var(--white)" stroke-width="1.1"/></svg>
    </div>

    <ul class="contacts">
      <li>555-318-6094</li>
      <li>555-742-0583</li>
      <li>velmarllc@tridomail.Com</li>
      <li>www.velmarllc.Com</li>
    </ul>
  </section>

</main>
</body>
</html>
```